Redesign of outdated "Automotive Automation Company"

We are looking to finally update our outdated website with some cutting edge graphics. We want our customers to know we value technology and are cutting edge as far as design. We provide automation solutions for the automotive industry which essentially means we program robots, and sell automation related products.

Current URL

http://lnk.vexor.test/Qm7trz
Updates

Project Deadline Extended
Reason: The client portal wasn't working, it's just finally been fixed by Pixel Harbor. I will go through and start reviewing designs.

We are trying to go with the same look and feel on our business cards, line cards, apparel, etc. so we are forming a brand. I have included the current draft of the line card. Please utilize our newest Logo TMV Standardized Logo.jpg http://img.pelvarhost.test/zq4Rb8d.jpg?1 Also we are trying hard to sell the following software / hardware companies so we can put some emphasis on their product. Corvane Systems https://www.corvanesystems.test/ We make money on selling the software and then on the integration. I think you should tie in this animation. ยท Shop Line Tangle to Throughput https://media.vidloft.test/deliveries/9b2e7c41d05f83a6c17e2d94b0a6f3e1c85d7b42.jpg?image_play_button=true&image_play_button_color=7b796ae0&image_crop_resized=275x155 In this 2-minute video, discover how Keystroke can help run your plant floor. We are Authorized Integrators / Resellers for Halbrook Controls Tavrin Sensorik http://tavrin.test/en/usa/ Corvane Systems https://www.corvanesystems.test/ Meridel Process Works www.mpwxx.test Solbry Belt Corp www.solbrybelt.test Quellmark Fabrication http://www.quellmarkfab.test/strategic_partners.aspx

Target Market(s)

Large automotive companies looking for automation or robotic programming. So Professional is key.

Industry/Entity Type

Automotive

Font styles to use
Other font styles liked:
• Possible Open Sans or Lato

Colors
0591cc
ceeaf6
fbd4d5
fbf289
fece3e

Requirements
Must have
• Professional Modern Design.

I want a homepage design, and a rough Sales Page... Where numerous products can be listed.
Nice to have
• Maybe an updated logo if possible.

```html
<!DOCTYPE html>
<html lang="en">
<head>
<meta charset="utf-8">
<title>TMV Engineering Solutions – Automation, Robotics, Controls</title>
<link href="https://fonts.googleapis.com/css2?family=Lato:wght@400;700;900&family=Open+Sans:wght@400;600;700&display=swap" rel="stylesheet">
<style>
:root{
  --pink:#e8185a;
  --pink-deep:#d7144f;
  --green:#8cc63f;
  --green-dark:#6fae2a;
  --green-text:#7dbb2e;
  --dark:#2b2b2b;
  --grey-bg:#f1f1f1;
  --text:#555;
  --white:#fff;
  --orange:#f4a11d;
  --cyan:#0591cc;
  --yellow:#fbf289;
}
*{margin:0;padding:0;box-sizing:border-box}
html,body{width:1200px;height:2803px;overflow:hidden}
body{position:relative;font-family:"Lato",sans-serif;color:var(--text);background:var(--white)}
.abs{position:absolute}
.center{left:0;width:1200px;text-align:center}

.stripe{top:0;left:0;width:1200px;height:6px;display:flex}
.stripe span{flex:1}

.header{top:6px;left:0;width:1200px;height:96px;background:var(--white);border-bottom:3px solid var(--pink)}
.brand{left:132px;top:22px;display:flex;align-items:center;gap:12px}
.brand-mark{width:52px;height:52px;border-radius:50%;background:var(--pink)}
.brand-name{font-weight:900;font-size:20px;line-height:22px;color:var(--dark)}
.contact-top{top:18px;font-size:19px;color:var(--pink);display:flex;align-items:center;gap:8px}
.contact-top.email{font-size:15px}
.nav{top:55px;left:637px;display:flex;font-family:"Open Sans",sans-serif;font-size:15px;font-weight:600}
.nav a{display:block;height:44px;line-height:44px;padding:0 22px;color:var(--dark);text-decoration:none}
.nav a.active{background:var(--pink);color:var(--white)}

.hero{top:102px;left:0;width:1200px;height:555px;background:linear-gradient(180deg,#6a6a6a,#4e4e4e)}
.hero-title{top:258px;font-weight:700;font-size:44px;letter-spacing:3px;color:var(--white)}
.hero-sub{top:325px;font-size:30px;color:#eee}
.btn{display:block;text-align:center;border-radius:30px;font-family:"Open Sans",sans-serif;text-transform:uppercase}
.hero-btn{top:395px;left:502px;width:194px;height:42px;line-height:38px;background:var(--green);border:2px solid var(--white);color:var(--white);font-size:16px}
.hero-arrow{top:300px;width:36px;height:80px;background:rgba(0,0,0,.45)}
.dots{top:618px;left:528px;display:flex;gap:8px}
.dots span{width:36px;height:4px;background:#888}
.dots span.on{background:var(--green)}

.welcome-title{top:700px;font-weight:900;font-size:25px;color:var(--dark)}
.welcome-rule{top:745px;left:560px;width:80px;height:3px;background:var(--green)}
.welcome-lede{top:762px;font-weight:700;font-size:20px;color:var(--green-text)}
.welcome-text{top:800px;left:153px;width:894px;text-align:center;font-size:14.5px;line-height:20px;color:#666}

.green-band{top:955px;left:0;width:1200px;height:294px;background:var(--green)}
.feature{top:925px;width:290px}
.feature-icon{width:50px;height:50px;border-radius:8px;background:var(--green-dark);border:3px solid var(--white);float:left;margin-right:14px;display:flex;align-items:center;justify-content:center}
.feature h3{font-size:17px;font-weight:700;color:var(--dark);line-height:22px;padding-top:2px}
.feature h3 span{display:block}
.feature p{clear:both;padding-top:16px;font-family:"Open Sans",sans-serif;font-size:13.5px;line-height:18px;color:var(--white)}
.more-btn{top:1186px;left:469px;width:262px;height:44px;line-height:44px;background:var(--dark);color:var(--white);font-size:17px}

.product{top:1249px;left:0;width:1200px;height:298px;background:var(--grey-bg)}
.product-media{top:1287px;left:132px;width:360px;height:224px;border:6px solid var(--white);box-shadow:0 1px 4px rgba(0,0,0,.2);background:linear-gradient(135deg,#e9eef1,#c9d3d9)}
.product-title{top:1290px;left:512px;font-weight:700;font-size:36px;color:#1d3c62}
.product-sub{top:1350px;left:518px;font-weight:700;font-size:19px;line-height:26px;color:var(--dark)}
.product-note{top:1406px;left:518px;font-weight:700;font-size:19px;color:var(--orange)}
.product-btn{top:1453px;left:522px;width:158px;height:38px;line-height:38px;background:var(--orange);color:var(--dark);font-size:14px;font-weight:600;text-transform:none}

.services{top:1547px;left:0;width:1200px;height:537px;background:linear-gradient(180deg,#ee2e6a,var(--pink-deep))}
.services-title{top:1594px;font-weight:900;font-size:25px;color:var(--white)}
.services-rule{top:1630px;left:560px;width:80px;height:2px;background:var(--white)}
.services-lede{top:1650px;font-weight:700;font-size:19px;color:var(--white)}
.services-text{top:1686px;left:160px;width:880px;text-align:center;font-weight:700;font-size:14.5px;line-height:20px;color:var(--white)}
.support{top:1782px;left:440px;width:335px;height:44px;line-height:44px;padding-left:46px;background:var(--dark);color:var(--white);font-size:18px;font-weight:600;text-transform:uppercase}
.support-ic{position:absolute;left:-14px;top:-4px;width:52px;height:52px;border-radius:50%;background:var(--white);border:4px solid var(--dark)}
.consult{top:1852px;font-weight:700;font-size:19px;color:var(--white)}
.svc-list{top:1898px;width:230px;list-style:none;font-family:"Open Sans",sans-serif;font-size:13px;line-height:23.5px;color:var(--white)}
.svc-list li::before{content:"› ";font-weight:700}

.partners-title{top:2128px;font-weight:900;font-size:25px;color:var(--dark)}
.robot{top:2087px;left:25px;width:103px;height:244px;background:linear-gradient(180deg,#f07b2a,#d25a10);border-radius:10px;opacity:.9}
.partner{top:2202px;height:76px;border:1px solid #ddd;background:var(--white);display:flex;align-items:center;justify-content:center;gap:8px;font-weight:700;font-size:15px;color:#333}
.partner i{width:16px;height:16px;background:#333;display:block}
.join-btn{top:2296px;left:553px;width:135px;height:42px;line-height:38px;border:2px solid var(--green);color:#444;font-size:17px}

.contact{top:2370px;left:0;width:1200px;height:382px;background:linear-gradient(135deg,var(--green),#7bb634)}
.field{left:132px;width:337px;height:36px;border-radius:18px;background:var(--white);font-family:"Open Sans",sans-serif;font-size:13px;color:#999;padding:9px 16px}
.submit{top:2686px;left:357px;width:109px;height:36px;line-height:32px;border:2px solid var(--white);background:var(--white);color:var(--dark);font-size:17px;font-weight:700}
.info-circle{top:2396px;left:573px;width:254px;height:254px;border-radius:50%;background:rgba(40,80,20,.45);color:var(--white);text-align:center;padding-top:58px}
.info-circle .ph{font-size:17px}
.info-circle .em{font-size:14px;margin-top:4px}
.info-circle .ad{font-size:12.5px;line-height:16px;margin-top:30px}
.social{left:938px;display:flex;align-items:center;gap:14px;font-family:"Open Sans",sans-serif;font-size:11px;color:#eef6e0;text-transform:uppercase}
.social span{width:38px;height:38px;border-radius:50%;background:var(--cyan);display:block}
.social span.rss{background:var(--orange)}

.footer{top:2752px;left:0;width:1200px;height:51px;background:var(--dark);color:#ddd;font-size:13px}
.footer .copy{position:absolute;left:132px;top:17px}
.pay{position:absolute;top:12px;display:flex;gap:6px;left:848px}
.pay span{height:26px;padding:0 7px;background:var(--white);color:#333;font-size:10px;font-weight:700;line-height:26px;border-radius:2px}
</style>
</head>
<body>

<div class="abs stripe"><span style="background:var(--pink)"></span><span style="background:var(--cyan)"></span><span style="background:var(--yellow)"></span><span style="background:#fece3e"></span><span style="background:var(--dark)"></span><span style="background:var(--pink)"></span><span style="background:var(--cyan)"></span><span style="background:var(--yellow)"></span></div>

<header class="abs header">
  <div class="abs brand"><span class="brand-mark"></span><div class="brand-name">TMV Engineering<br>Solutions, Inc.</div></div>
  <div class="abs contact-top" style="left:636px">
    <svg width="16" height="18" viewBox="0 0 16 18"><path d="M3 1h3l1 4-2 1.5c1 2 2.5 3.5 4.5 4.5L11 9l4 1v3c0 1-1 2-2 2C7 15 1 9 1 3c0-1 1-2 2-2z" fill="var(--pink)"/></svg>123-456-7890</div>
  <div class="abs contact-top email" style="left:798px">
    <svg width="18" height="13" viewBox="0 0 18 13"><rect x="0.5" y="0.5" width="17" height="12" fill="var(--pink)"/><path d="M1 1l8 6 8-6" stroke="#fff" fill="none"/></svg>info@tmvengineering.test</div>
  <nav class="abs nav"><a class="active">HOME</a><a>ABOUT US</a><a>SERVICES</a><a>CONTACT US</a></nav>
</header>

<section class="abs hero" role="img" aria-label="Line sketch of a control network: PLCs, client computers, a robot, SQL databases and any device joined by lines"></section>
<h1 class="abs center hero-title">AUTOMATION &nbsp;·&nbsp; ROBOTICS &nbsp;·&nbsp; CONTROLS</h1>
<p class="abs center hero-sub">Your Premier Automation Consulting &amp; Systems Integration choice!</p>
<a class="abs btn hero-btn">Check our work</a>
<div class="abs hero-arrow" style="left:0"><svg width="36" height="80"><path d="M22 30l-10 10 10 10" stroke="#fff" stroke-width="3" fill="none"/></svg></div>
<div class="abs hero-arrow" style="left:1164px"><svg width="36" height="80"><path d="M14 30l10 10-10 10" stroke="#fff" stroke-width="3" fill="none"/></svg></div>
<div class="abs dots"><span class="on"></span><span></span><span></span></div>

<h2 class="abs center welcome-title">WELCOME TO TMV</h2>
<div class="abs welcome-rule"></div>
<p class="abs center welcome-lede">Helping your business optimize its Automation....</p>
<p class="abs welcome-text">Industrial Automation is constantly evolving with ever-changing technological breakthroughs. For companies to remain competitive, they need to be more nimble than ever implementing productivity and manufacturing innovations. But identifying and implementing the right Automation, Robotics and industrial Controls is never easy. That's where our team of experts comes in to play bringing our proven experience to the table.</p>

<div class="abs green-band"></div>
<div class="abs feature" style="left:132px">
  <div class="feature-icon"><svg width="26" height="20"><circle cx="13" cy="6" r="4" fill="#fff"/><path d="M5 19c0-5 4-7 8-7s8 2 8 7z" fill="#fff"/></svg></div>
  <h3>Get to know<span>Our Team approach</span></h3>
  <p>Lorem ipsum dolor sit amet, consectetuer adipiscing elit, sed diam nonummy nibh euismod tincidunt ut laoreet dolore magna aliquam erat volutpat. Ut wisi enim ad minim veniam, quis nostrud exerci tation ullamcorper suscipit lobortis nisl ut aliquip ex ea commodo consequat.</p>
</div>
<div class="abs feature" style="left:451px">
  <div class="feature-icon"><svg width="26" height="26"><circle cx="13" cy="13" r="7" stroke="#fff" stroke-width="4" fill="none" stroke-dasharray="4 3"/><circle cx="13" cy="13" r="3" fill="#fff"/></svg></div>
  <h3>This way to<span>Automation success</span></h3>
  <p>Lorem ipsum dolor sit amet, consectetuer adipiscing elit, sed diam nonummy nibh euismod tincidunt ut laoreet dolore magna aliquam erat volutpat. Ut wisi enim ad minim veniam, quis nostrud exerci tation ullamcorper suscipit lobortis nisl ut aliquip ex ea commodo consequat.</p>
</div>
<div class="abs feature" style="left:775px">
  <div class="feature-icon"><svg width="26" height="22"><rect x="3" y="12" width="4" height="8" fill="#fff"/><rect x="11" y="7" width="4" height="13" fill="#fff"/><rect x="19" y="2" width="4" height="18" fill="#fff"/></svg></div>
  <h3>Bring great ideas<span>To your business</span></h3>
  <p>Lorem ipsum dolor sit amet, consectetuer adipiscing elit, sed diam nonummy nibh euismod tincidunt ut laoreet dolore magna aliquam erat volutpat. Ut wisi enim ad minim veniam, quis nostrud exerci tation ullamcorper suscipit lobortis nisl ut aliquip ex ea commodo consequat.</p>
</div>
<a class="abs btn more-btn">Know more about us</a>

<section class="abs product"></section>
<div class="abs product-media" role="img" aria-label="Video still for the Keystroke 7.7 release with a version badge"></div>
<h2 class="abs product-title">The New Keystroke v7.7</h2>
<p class="abs product-sub">Cross-Platform Freedom,<br>Game-Changing New Features</p>
<p class="abs product-note">Discover The New SCADA, Now With Over 40 Added Features</p>
<a class="abs btn product-btn">Start Learning Now</a>

<section class="abs services"></section>
<h2 class="abs center services-title">Our Services</h2>
<div class="abs services-rule"></div>
<p class="abs center services-lede">Bring our experts to your business</p>
<p class="abs services-text">We offer a range of engineering services - all designed to help your company reach its full potential. Whether you're looking for a small tweak, complete overhaul or a new installation we have you covered. Whatever your situation and the challenges you face, we have solutions.</p>
<div class="abs btn support"><span class="support-ic"></span>We offer 24 hour support !</div>
<p class="abs center consult">We offer consulting / integration for</p>
<ul class="abs svc-list" style="left:132px"><li>Industrial Automation</li><li>Robotics</li><li>Controls Engineering</li><li>Project Management</li><li>Training</li><li>Systems Integration</li></ul>
<ul class="abs svc-list" style="left:377px"><li>Custom Automated Equipment</li><li>2D / 3D CAD Capabilities</li><li>3D Robotic Simulation</li><li>PLC Programming</li><li>SCADA Design &amp; Programming</li><li>HMI Design &amp; Programming</li></ul>
<ul class="abs svc-list" style="left:599px"><li>Industrial Automation</li><li>Robotics</li><li>Controls Engineering</li><li>Project Management</li><li>Training</li><li>Systems Integration</li></ul>
<ul class="abs svc-list" style="left:836px"><li>Custom Automated Equipment</li><li>2D / 3D CAD Capabilities</li><li>3D Robotic Simulation</li><li>PLC Programming</li><li>SCADA Design &amp; Programming</li><li>HMI Design &amp; Programming</li></ul>

<h2 class="abs center partners-title">We are Authorized Integrators / Resellers for</h2>
<div class="abs robot" role="img" aria-label="Orange industrial robot arm"></div>
<div class="abs partner" style="left:132px;width:156px"><i></i>Verquent</div>
<div class="abs partner" style="left:298px;width:156px"><i></i>Corvane Systems</div>
<div class="abs partner" style="left:466px;width:281px"><i></i>Meridel Process Works</div>
<div class="abs partner" style="left:757px;width:142px">Solbry Belt Corp</div>
<div class="abs partner" style="left:912px;width:158px;font-size:13px">Quellmark Fabrication</div>
<a class="abs btn join-btn">Join them</a>

<section class="abs contact"></section>
<h2 class="abs" style="top:2414px;left:132px;font-weight:700;font-size:25px;color:#fff">Quick Contact</h2>
<div class="abs field" style="top:2469px">Your Name</div>
<div class="abs field" style="top:2516px">Your email address</div>
<div class="abs field" style="top:2563px">Your phone number</div>
<div class="abs field" style="top:2610px;height:64px;border-radius:14px">Your message</div>
<a class="abs btn submit">Submit</a>
<div class="abs info-circle">
  <div class="ph">123.456.7890</div>
  <div class="em">info@tmvengineering.test</div>
  <div class="ad">TMV Engineering Solutions, Inc.<br>472 Westbrook Ave. Suite C<br>Larkton, MI 48790</div>
</div>
<h2 class="abs" style="top:2414px;left:938px;font-weight:700;font-size:25px;color:#fff">Follow Us</h2>
<div class="abs social" style="top:2466px"><span></span>Friendspace</div>
<div class="abs social" style="top:2524px"><span></span>Chirpline</div>
<div class="abs social" style="top:2582px"><span></span>Worklink</div>
<div class="abs social" style="top:2640px"><span class="rss"></span>RSS Feed</div>

<footer class="abs footer">
  <span class="copy">Copyright 2015 TMV Engineering Solutions. All rights reserved.</span>
  <div class="pay"><span>Paywell</span><span>Vantra</span><span>Vantra Go</span><span>Meritcard</span><span>Mestra</span></div>
</footer>

</body>
</html>
```